BrivoMatex. Lantern for the Steady Growth. Business card

Professional business card for BrivoMatex (Lantern for the Steady Growth)
My rationale: Strategy-> Execution-> Results-> Value that lead to the BrivoMatex name: We put the Lantern for the Steady Growth.
We deliver value to our customers helping them at defining a good strategy (cyan arrow). 90% of well formulated strategies fail due to poor execution so we also consider strategical execution very important (green arrow). Due to the execution we obtain the results (blue arrow). Finally, the results provide feedback to redefine strategy, and the new strategy has to be executed and new results obtained providing new feedback and on and on. It's like a wheel that finally, must create corporate value: value for shareholders, staholders, employees, providers...-

Target Market(s)

CEOs and steering comitees , invewrnent funds

Industry/Entity Type

Business Consultant

Contact Information for Business Card

Tommaso Ferlini
CEO & Founder
tommaso.ferlini@brivomatex.example
Mobile: +34 611.205.938
www.brivomatex.example

Colors

Designer to choose colors to be used in the design.

Requirements
Nice to have
• Nice to hace the words: Strategy, execution, results
• Nice to vave the claim: Lantern for the Steady Growth
• The three colors should be shown:
• cyan for STRATEGY
• green for EXECUTION
• blue for RESULTS
Should not have
• Complete black background

```html
<!DOCTYPE html>
<html lang="en">
<head>
<meta charset="utf-8">
<title>BrivoMatex — Business Card</title>
<link rel="stylesheet" href="https://fonts.googleapis.com/css2?family=Fira+Sans+Extra+Condensed:wght@700&family=Roboto+Condensed:wght@300;400;700&display=swap">
<style>
  :root {
    --page-bg: #ececec;
    --card-cyan: #00aeef;
    --ink-white: #ffffff;
    --ink-soft: #3fc4f4;
    --rule-light: #5fd2ff;
  }
  * { margin: 0; padding: 0; box-sizing: border-box; }
  html, body {
    width: 1200px;
    height: 913px;
    overflow: hidden;
    background: var(--page-bg);
  }
  .canvas {
    position: relative;
    width: 1200px;
    height: 913px;
  }
  .business-card {
    position: absolute;
    left: 432px;
    top: 162px;
    width: 336px;
    height: 589px;
    background: var(--card-cyan);
    color: var(--ink-white);
    font-family: "Roboto Condensed", "Arial Narrow", sans-serif;
  }
  .brand-mark {
    position: absolute;
    left: 133px;
    top: 205px;
    width: 70px;
    height: 70px;
    border-radius: 50%;
    background: var(--ink-white);
  }
  .brand-name {
    position: absolute;
    left: 0;
    right: 0;
    top: 292px;
    text-align: center;
    font-family: "Fira Sans Extra Condensed", "Arial Narrow", sans-serif;
    font-weight: 700;
    font-size: 62px;
    line-height: 1;
    letter-spacing: -1px;
  }
  .holder {
    position: absolute;
    right: 25px;
    top: 370px;
    text-align: right;
  }
  .holder-name {
    font-weight: 700;
    font-size: 22px;
    line-height: 26px;
  }
  .holder-role {
    font-weight: 300;
    font-size: 16px;
    line-height: 20px;
    color: var(--ink-soft);
  }
  .contact {
    position: absolute;
    right: 25px;
    top: 450px;
    text-align: right;
    font-weight: 300;
    font-size: 21px;
    line-height: 22px;
    letter-spacing: -0.3px;
  }
  .contact p { white-space: nowrap; }
  .contact .phone { margin-bottom: 3px; }
  .card-rule {
    position: absolute;
    left: 33px;
    width: 272px;
    top: 553px;
    height: 2px;
    background: var(--rule-light);
  }
  .claim {
    position: absolute;
    left: 31px;
    width: 278px;
    top: 565px;
    display: flex;
    justify-content: space-between;
    font-size: 13px;
    letter-spacing: 2.2px;
    color: var(--rule-light);
    white-space: nowrap;
  }
</style>
</head>
<body>
<main class="canvas">
  <section class="business-card" aria-label="BrivoMatex business card">
    <div class="brand-mark" aria-hidden="true"></div>
    <h1 class="brand-name">BrivoMatex</h1>

    <div class="holder">
      <p class="holder-name">Tommaso FERLINI</p>
      <p class="holder-role">CEO &amp; Founder</p>
    </div>

    <div class="contact">
      <p class="phone">+34 611 205 938</p>
      <p class="email">tommaso.ferlini@brivomatex.example</p>
      <p class="web">www.brivomatex.example</p>
    </div>

    <div class="card-rule" aria-hidden="true"></div>
    <p class="claim"><span>STRATEGY</span><span>·</span><span>EXECUTION</span><span>·</span><span>RESULTS</span></p>
  </section>
</main>
</body>
</html>
```